Lucia''s Blue Pantry - blog, shop and recipes - web design

I will be using wordpress and need a website developed to allow me to do daily blogs of recipes and food comments, an index of my recipes and a shop where people can buy my products including food (pasta and sauce kits, cannoli, biscotti) and my upcoming unique aprons for example. I have already selected a logo which I have copied the files to this brief.

The feel of the entire site should be modern but classic and clean. The main colour of the site should be red and the same red as my logo. I will eventually include a photo of myself and I would like the home page to read; Lucia Marbetto in (insert logo) Lucia's Blue Pantry

Home page:
1. Needs to allow me to write daily updates on what I'm cooking or eating etc. and include upload of photos of food.
2. Needs an index/link to recipes broken down into: Antipasto, Starters, Sides, Mains, Desserts, Thermomix Recipes.
3. Needs to have the following links: Home, Recipes, About, Contact us, Shop, Events, Travel. All of these links will need separate pages with links to other pages etc.
4. There should also be icons for links to email, facebook, pinterest, and twitter. It should say Follow Me! or Connect with Me!

Recipe pages:
1. Need to have a template to enter recipes and photos.

About Page:
1. Will have my story.

Contact us page:
1. Contact details to be provided.

Events
1. This will contain news and events like cooking classes that I will be holding.

Shop:
1. This page will need to allow items to be purchased and paid for via paypal.

Travel:
1. This page will include photos and information on food related places I have travelled.

Please do not hesitate to contact me if you need any further information.

Requirements
Should not have
• This is NOT a restaurant or cafe and therefore should not include links or headers such as business hours or menu.

```html
<!DOCTYPE html>
<html lang="en">
<head>
<meta charset="utf-8">
<title>Lucia's Blue Pantry – Latest Columns</title>
<link rel="stylesheet" href="https://fonts.googleapis.com/css2?family=Great+Vibes&family=Questrial&family=Open+Sans:wght@400;600&display=swap">
<style>
  :root {
    --page-bg: #fdfcf5;
    --brand-red: #d90000;
    --accent-gold: #e3ae22;
    --date-gold: #e7a81c;
    --ink: #222222;
    --body-ink: #444444;
    --rule: #dddddd;
    --pager-grey: #a9a9a9;
    --footer-grey: #c9c9c9;
  }
  * { margin: 0; padding: 0; box-sizing: border-box; }
  html, body { width: 1200px; height: 2174px; overflow: hidden; }
  body {
    position: relative;
    background: var(--page-bg);
    font-family: "Open Sans", sans-serif;
    color: var(--body-ink);
  }
  .section-title {
    position: absolute; left: 128px; top: 12px;
    font-family: "Great Vibes", cursive;
    font-size: 38px; font-weight: 400; color: var(--brand-red);
  }
  .post { position: absolute; left: 128px; width: 700px; }
  .post-photo { position: absolute; }
  .post-title {
    position: absolute; left: 0; white-space: nowrap;
    font-family: "Questrial", sans-serif; font-weight: 400;
    font-size: 28px; color: var(--ink);
  }
  .post-date { color: var(--date-gold); }
  .post-meta {
    position: absolute; left: 0; font-size: 12px; color: var(--ink);
  }
  .post-meta .category { color: var(--brand-red); }
  .post-excerpt {
    position: absolute; left: 0; width: 690px;
    font-size: 11.6px; line-height: 16.5px; color: var(--body-ink);
  }
  .read-more {
    position: absolute; left: 0; width: 102px; height: 36px;
    background: var(--brand-red); color: #fff;
    font-family: "Questrial", sans-serif; font-size: 16px;
    display: flex; align-items: center; justify-content: center;
    text-decoration: none;
  }
  .divider {
    position: absolute; left: 110px; top: 1986px; width: 735px;
    height: 1px; background: #bdbdbd;
  }
  .pager {
    position: absolute; left: 329px; top: 2009px;
    display: flex; gap: 4px; list-style: none;
  }
  .pager li {
    width: 34px; height: 33px; background: var(--pager-grey);
    color: #f3f3f3; font-size: 12px;
    display: flex; align-items: center; justify-content: center;
  }
  .pager li.current { background: var(--brand-red); color: #fff; }
  .widget { position: absolute; left: 875px; width: 220px; }
  .widget-title {
    height: 40px; padding-left: 13px;
    font-family: "Questrial", sans-serif; font-weight: 400;
    font-size: 21px; color: #fff;
    display: flex; align-items: center;
  }
  .widget-title.red { background: var(--brand-red); }
  .widget-title.gold { background: var(--accent-gold); }
  .widget-list { list-style: none; margin-top: 12px; }
  .widget-list li {
    height: 31px; border-bottom: 1px solid var(--rule);
    font-size: 11.6px; color: var(--ink);
    display: flex; align-items: center; padding-left: 12px;
  }
  .widget-list li::before {
    content: "›"; color: #888; font-size: 12px; margin-right: 10px;
  }
  .site-footer {
    position: absolute; left: 0; top: 2103px; width: 1200px; height: 71px;
    background: var(--footer-grey);
  }
  .footer-nav {
    position: absolute; left: 131px; top: 21px;
    display: flex; list-style: none; font-size: 13px; color: var(--ink);
  }
  .footer-nav li + li::before { content: "|"; margin: 0 15px; }
  .footer-call {
    position: absolute; left: 716px; top: 21px; font-size: 13px; color: var(--ink);
  }
  .footer-call .phone { color: var(--brand-red); }
  .payment-badge {
    position: absolute; left: 988px; top: 9px; width: 107px; height: 46px;
    background: #f6e6a6; border-radius: 6px;
  }
</style>
</head>
<body>

<main>
  <h1 class="section-title">Latest Coloumns</h1>

  <article class="post" style="top:67px">
    <div class="post-photo" role="img" aria-label="Slice of pizza with tomatoes, basil and red onions on a wooden board"
      style="left:0;top:0;width:696px;height:445px;background:radial-gradient(ellipse at 45% 60%, #d69a52 0%, #a5643a 40%, #5e3a22 100%);"></div>
    <h2 class="post-title" style="top:465px"><span class="post-date">02 Jul</span> Spinach Shallot and Pizza Marghetita</h2>
    <p class="post-meta" style="top:504px"><span class="category">Cooking</span> | Lucia Admin</p>
    <p class="post-excerpt" style="top:535px">Garden Fresh and Packed with Flavor. It doesn't get better than homemade pizza. Here spinach, shallot, and feta come together in perfect unison creating a delightful pizza great for any lunch or dinner.&nbsp;&nbsp; 5.0 from 1 reviews Spinach Shallot and Feta Grilled Pizza Print Prep...</p>
    <a class="read-more" href="#" style="top:611px">Read More</a>
  </article>

  <article class="post" style="top:755px">
    <div class="post-photo" role="img" aria-label="Tortilla chips around bowls of guacamole and salsa on dark wood"
      style="left:132px;top:0;width:432px;height:417px;background:radial-gradient(circle at 50% 50%, #e8b04a 0%, #d9952f 42%, #5a4034 64%, #3f2d25 100%);"></div>
    <h2 class="post-title" style="top:457px"><span class="post-date">02 Jul</span> Spinach Special home Made Tomato Sauce</h2>
    <p class="post-meta" style="top:497px"><span class="category">Cooking</span> | Lucia Admin</p>
    <p class="post-excerpt" style="top:528px">Garden Fresh and Packed with Flavor. It doesn't get better than homemade pizza. Here spinach, shallot, and feta come together in perfect unison creating a delightful pizza great for any lunch or dinner.&nbsp;&nbsp; 5.0 from 1 reviews Spinach Shallot and Feta Grilled Pizza Print Prep...</p>
    <a class="read-more" href="#" style="top:602px">Read More</a>
  </article>

  <article class="post" style="top:1437px">
    <div class="post-photo" role="img" aria-label="Bowl of pasta with basil and tomatoes on a wooden table"
      style="left:106px;top:0;width:458px;height:290px;background:radial-gradient(ellipse at 50% 50%, #e9e2d6 0%, #d7b98f 45%, #c49c6c 100%);"></div>
    <h2 class="post-title" style="top:321px"><span class="post-date">02 Jul</span> Spinach Special home Made Tomato Sauce</h2>
    <p class="post-meta" style="top:362px"><span class="category">Cooking</span> | Lucia Admin</p>
    <p class="post-excerpt" style="top:393px">Garden Fresh and Packed with Flavor. It doesn't get better than homemade pizza. Here spinach, shallot, and feta come together in perfect unison creating a delightful pizza great for any lunch or dinner.&nbsp;&nbsp; 5.0 from 1 reviews Spinach Shallot and Feta Grilled Pizza Print Prep...</p>
    <a class="read-more" href="#" style="top:468px">Read More</a>
  </article>

  <div class="divider"></div>

  <ul class="pager">
    <li></li><li class="current">1</li><li>2</li><li>3</li><li>4</li><li>5</li><li>6</li><li></li>
  </ul>
</main>

<aside>
  <section class="widget" style="top:34px">
    <h3 class="widget-title red">Categories</h3>
    <ul class="widget-list">
      <li>Aenean non ummy hendreriauris</li><li>Consec tetuer adipiscing</li><li>Et magis dis parturient monte</li><li>Fusce feugiatle suada odio</li><li>Lorem ipsum dolor sit amet</li><li>Morbi nunc odio gravida at</li><li>Nascetur ridiculus mus</li><li>Phasellllus portausce suscipit</li><li>Praesent vestibu lum molestie</li><li>Varius mium sociis totdnatibus</li>
    </ul>
  </section>
  <section class="widget" style="top:441px">
    <h3 class="widget-title gold">Popular</h3>
    <ul class="widget-list">
      <li>Aenean non ummy hendreriauris</li><li>Consec tetuer adipiscing</li><li>Et magis dis parturient monte</li><li>Fusce feugiatle suada odio</li><li>Lorem ipsum dolor sit amet</li><li>Morbi nunc odio gravida at</li><li>Nascetur ridiculus mus</li><li>Phasellllus portausce suscipit</li><li>Praesent vestibu lum molestie</li><li>Varius mium sociis totdnatibus</li>
    </ul>
  </section>
  <section class="widget" style="top:829px">
    <h3 class="widget-title red">Recent Post</h3>
    <ul class="widget-list">
      <li>Aenean non ummy hendreriauris</li><li>Consec tetuer adipiscing</li><li>Et magis dis parturient monte</li><li>Fusce feugiatle suada odio</li><li>Lorem ipsum dolor sit amet</li><li>Morbi nunc odio gravida at</li><li>Nascetur ridiculus mus</li><li>Phasellllus portausce suscipit</li><li>Praesent vestibu lum molestie</li><li>Varius mium sociis totdnatibus</li>
    </ul>
  </section>
</aside>

<footer class="site-footer">
  <ul class="footer-nav">
    <li>Home</li><li>About</li><li>Recipes</li><li>Shop</li><li>Events</li><li>Travel</li>
  </ul>
  <p class="footer-call">Call us now toll free: <span class="phone">(800) 555-0142</span></p>
  <div class="payment-badge" aria-hidden="true"></div>
</footer>

</body>
</html>
```